Tallow Creek Advisory Business Card

Hi Morwen. Thank you for your work on my coaching business card. I have another business which needs a new card. It is my counselling business. The best way to find out how to approach this project will be to go to my other website. www.tallowcreekadvisory.com.au and you will be able to see the colours scheme that I will require. White, Green and blue.

The tag line is Tallow Creek Advisory So you can step ahead with ease. The clients are varied but mostly middle class Australian. The card is to show on it the same details as my other business card but with a different phone number. The tag lines are obviously different. The phone number is 9137 2564 The addresses are all the same.

Again simple, professional sophisticated is best.

```html
<!DOCTYPE html>
<html lang="en">
<head>
<meta charset="utf-8">
<title>Tallow Creek Advisory – Business Card</title>
<link rel="stylesheet" href="https://fonts.googleapis.com/css2?family=Josefin+Sans:wght@300;400&family=Work+Sans:wght@400&display=swap">
<style>
  :root {
    --bg: #e7e8ea;
    --card: #ffffff;
    --blue: #7aa7dc;
    --blue-deep: #5b8fd0;
    --green: #8cc63f;
    --ink: #1d1d1f;
    --ink-soft: #333336;
    --shade: #ececee;
  }
  * { box-sizing: border-box; margin: 0; padding: 0; }
  html, body { width: 1200px; height: 1000px; overflow: hidden; }
  body {
    background: var(--bg);
    font-family: "Work Sans", Arial, sans-serif;
    position: relative;
  }
  .card {
    position: absolute;
    left: 220px;
    width: 760px;
    height: 434px;
    background: var(--card);
    box-shadow: 0 6px 18px rgba(0,0,0,0.12);
    overflow: hidden;
  }
  .card--details { top: 44px; background: linear-gradient(180deg, var(--card) 0%, var(--card) 55%, var(--shade) 100%); }
  .card--front { top: 522px; }

  /* details side */
  .brand-name {
    font-family: "Josefin Sans", Arial, sans-serif;
    font-weight: 400;
    color: var(--blue);
    white-space: nowrap;
  }
  .card--details .brand-name { position: absolute; left: 40px; top: 34px; font-size: 38px; }
  .card--details .tagline {
    position: absolute; left: 42px; top: 82px;
    font-family: "Josefin Sans", Arial, sans-serif; font-weight: 400;
    font-size: 15px; letter-spacing: 0.6px; color: var(--green);
  }
  .person-name {
    position: absolute; right: 40px; top: 112px;
    font-family: "Work Sans", Arial, sans-serif;
    font-size: 36px; color: var(--ink);
  }
  .divider {
    position: absolute; left: 0; right: 0; top: 160px; height: 4px;
    background: linear-gradient(90deg, rgba(140,198,63,0.6), var(--green) 40%, var(--green));
  }
  .role {
    position: absolute; right: 40px; top: 174px;
    font-size: 17px; color: var(--ink-soft);
  }
  .contacts { position: absolute; left: 42px; top: 226px; list-style: none; }
  .contacts li {
    display: flex; align-items: center; gap: 9px;
    font-size: 17px; color: var(--ink); line-height: 27px;
  }
  .contacts svg { width: 15px; height: 15px; fill: var(--ink); }
  .offices { position: absolute; left: 42px; top: 322px; list-style: none; }
  .offices li { font-size: 16px; color: var(--ink); line-height: 27px; }

  /* front side */
  .front-logo { position: absolute; left: 60px; right: 60px; top: 96px; }
  .card--front .brand-name { font-size: 60px; line-height: 1; }
  .front-rule { margin-top: 16px; height: 2px; width: 100%; background: var(--green); }
  .card--front .tagline {
    margin-top: 12px;
    font-family: "Josefin Sans", Arial, sans-serif; font-weight: 300;
    font-size: 25px; letter-spacing: 2px; color: var(--blue);
    white-space: nowrap;
  }
  .services {
    position: absolute; left: 60px; right: 40px; bottom: 46px;
    font-size: 23px; color: var(--blue-deep); line-height: 34px;
    white-space: nowrap;
  }
  .services .dot { color: var(--green); padding: 0 6px; }
</style>
</head>
<body>

<section class="card card--details" aria-label="Business card, contact side">
  <div class="brand-name">Tallow Creek Advisory</div>
  <div class="tagline">SO YOU CAN STEP AHEAD WITH EASE</div>
  <div class="person-name">Neil Hartigan</div>
  <div class="divider"></div>
  <div class="role">Clinical Psychotherapist and Executive Coach</div>

  <ul class="contacts">
    <li>
      <svg viewBox="0 0 16 16" aria-hidden="true"><path d="M2 5c0-2 2-3 6-3s6 1 6 3v1h-3V5H5v1H2zM4 7h8l2 6H2zM8 8.5a2 2 0 100 4 2 2 0 000-4z"/></svg>
      +612 9137 2564
    </li>
    <li>
      <svg viewBox="0 0 16 16" aria-hidden="true"><path d="M1 3h14v10H1zM2.5 4.5v.4L8 9l5.5-4.1v-.4z"/></svg>
      info@tallowcreekadvisory.com.au
    </li>
    <li>
      <svg viewBox="0 0 16 16" aria-hidden="true"><path d="M8 1a7 7 0 100 14A7 7 0 008 1zm0 1.5c.9 0 1.8 1.6 2.1 4H5.9C6.2 4.1 7.1 2.5 8 2.5zM2.6 7h2.3a12 12 0 000 2H2.6a5.6 5.6 0 010-2zm3.3 2.5h4.2c-.3 2.4-1.2 4-2.1 4s-1.8-1.6-2.1-4zM11.1 7h2.3a5.6 5.6 0 010 2h-2.3a12 12 0 000-2z"/></svg>
      www.tallowcreekadvisory.com.au
    </li>
  </ul>

  <ul class="offices">
    <li>Fenwick Office: 152 Fenwick Point Road Fenwick</li>
    <li>Northbank Office: Suite 104 / 58 Larkin Street Northbank</li>
    <li>Ashgrove Street Office: Suite 3, 61 Ashgrove Street Sydney</li>
  </ul>
</section>

<section class="card card--front" aria-label="Business card, front side">
  <div class="front-logo">
    <div class="brand-name">Tallow Creek Advisory</div>
    <div class="front-rule"></div>
    <div class="tagline">SO YOU CAN STEP AHEAD WITH EASE</div>
  </div>
  <p class="services">
    Relationships Counselling<span class="dot">•</span>Drug and Alcohol Counselling<br>
    Confidence Coaching<span class="dot">•</span>Life Coaching<span class="dot">•</span>Executive Coaching
  </p>
</section>

</body>
</html>
```